Home page makeover

Take my existing home page, www.maplecrestledger.com and redesign layout to look more current considering today's touch design prevalence.
Reuse existing elements or suggest improved ones if available.
I generally have average CSS and HTML skills using div containers, defining lists and using columns to create the code to support the layout.
Updates
Just wanted to send out a quick message to thank all of you for your submissions. Many of you offered nice designs, but unfortunately could only choose one.
Target Market(s)
Generally targeting individuals with some assets for retirement. Basically your average working professional or business owner.
Industry/Entity Type
It Support
Look and feel
Each slider illustrates characteristics of the customer's brand and the style your logo design should communicate.

```html
<!DOCTYPE html>
<html lang="en">
<head>
<meta charset="utf-8">
<title>Maplecrest Ledger – Home</title>
<link rel="stylesheet" href="https://fonts.googleapis.com/css2?family=Cinzel:wght@400;700&family=Open+Sans:wght@400;600&display=swap">
<style>
:root{
  --page:#f6f6f4;
  --green:#a4bf3c;
  --green-dark:#2f4f1f;
  --ink:#333333;
  --muted:#6b6b6b;
  --panel:#3a3a3a;
  --price:#c4dc3f;
}
*{box-sizing:border-box;margin:0;padding:0}
html,body{width:711px;height:1200px;overflow:hidden}
body{position:relative;background:var(--page);font-family:"Open Sans",Arial,sans-serif;color:var(--ink)}
.abs{position:absolute}
.serif{font-family:"Cinzel",Georgia,serif}

.header{left:0;top:0;width:711px;height:82px;background:var(--page);border-bottom:3px solid #111}
.brand{left:70px;top:22px;display:flex;align-items:center;gap:8px}
.brand-mark{width:14px;height:14px;background:var(--green-dark)}
.brand-name{font-family:"Cinzel",Georgia,serif;font-size:17px;font-weight:700;color:var(--green-dark);line-height:1}
.brand-tag{left:92px;top:44px;font-size:7px;color:var(--green-dark);font-style:normal}
.auth{top:13px;height:16px;width:57px;font-family:"Cinzel",Georgia,serif;font-size:7px;color:#fff;display:flex;align-items:center;justify-content:center}
.auth.up{left:522px;background:var(--green-dark)}
.auth.in{left:583px;background:var(--green)}
.nav{top:50px;left:345px;display:flex;height:32px;font-family:"Cinzel",Georgia,serif;font-size:9px}
.nav a{color:var(--ink);text-decoration:none;display:flex;align-items:center;padding:0 11px}
.nav a.active{background:var(--green);color:#fff;width:59px;justify-content:center;padding:0}

.hero{left:0;top:85px;width:711px;height:320px;background:linear-gradient(180deg,#c9a45c 0%,#f2d98a 30%,#f6e6a3 50%,#d9b155 72%,#b48a34 100%)}
.promo{left:70px;top:223px;width:231px;height:96px;background:var(--panel);color:#eee;padding:18px 0 0 15px;font-size:11px;line-height:20px}
.promo b{color:var(--price);font-weight:600}
.promo .cta{display:inline-block;margin-top:8px;background:var(--green);color:#fff;font-weight:600;font-size:10.5px;padding:0 8px;line-height:17px}
.dots{left:335px;top:380px;display:flex;gap:3px}
.dots i{width:9px;height:9px;border-radius:50%;background:#444}
.dots i.on{background:var(--green)}

h2{font-family:"Cinzel",Georgia,serif;font-weight:700;font-size:11.5px;color:var(--green-dark);letter-spacing:.3px}
.center{left:0;width:711px;text-align:center}
.intro{left:77px;top:455px;width:557px;font-size:6.6px;line-height:14px;color:var(--muted);text-align:center}

.service{top:553px;width:178px}
.service h3{font-family:"Cinzel",Georgia,serif;font-weight:400;font-size:9px;color:var(--ink);margin-bottom:6px}
.service .photo{width:178px;height:112px;border:1px solid #ccc}
.service p{margin-top:11px;font-size:6.6px;line-height:14px;color:var(--muted)}
.more{display:inline-block;margin-top:8px;background:var(--green);color:#fff;font-family:"Cinzel",Georgia,serif;font-size:7px;padding:0 6px;line-height:16px}

.video{left:78px;top:846px;width:330px;height:178px;background:linear-gradient(135deg,#a9c46a,#e8e1c8 45%,#f4efe2 60%,#9bb55a)}
.features{left:418px;top:850px;width:220px;list-style:none}
.features li{display:flex;gap:9px;font-size:6.6px;line-height:10.5px;color:var(--ink);margin-bottom:9px}
.features svg{flex:none;margin-top:1px}

.quote{top:1084px;font-size:11px;color:var(--ink)}
.quote .who{font-size:12.5px;color:var(--green-dark)}
.quote .who b{font-weight:600;font-size:11px}

.footer{left:0;top:1137px;width:711px;height:63px;background:var(--green);color:#fff}
.foot-links{left:77px;top:1155px;font-family:"Cinzel",Georgia,serif;font-size:7.5px;word-spacing:3px}
.copyright{left:77px;top:1175px;font-family:"Cinzel",Georgia,serif;font-size:7px}
.social{top:1160px;width:20px;height:20px;border-radius:50%;background:#fff}
</style>
</head>
<body>
<header class="abs header">
  <div class="abs brand"><span class="brand-mark"></span><span class="brand-name">Maplecrest Ledger</span></div>
  <a class="abs auth up">SIGN UP</a>
  <a class="abs auth in">SIGN IN</a>
  <nav class="abs nav">
    <a class="active">HOME</a><a>ABOUT US</a><a>SERVICES</a><a>FAQ'S</a><a>CONTACT</a>
  </nav>
</header>

<section class="abs hero" role="img" aria-label="Man with raised arms standing in a golden wheat field at sunrise"></section>
<div class="abs promo">
  Only <b>$19.99</b> For a One Year Membership<br>
  Only <b>$9.99</b> Per Year After That<br>
  <span class="cta">SIGN UP</span>
</div>
<div class="abs dots"><i class="on"></i><i></i><i></i><i></i></div>

<h2 class="abs center" style="top:428px">WELCOME TO MAPLECREST LEDGER</h2>
<p class="abs intro">Lorem Ipsum is simply dummy text of the printing and typesetting industry. Lorem Ipsum has been the industry's standard dummy text ever since the 1500s, when an unknown printer took a galley of type and scrambled it to make a type specimen book. It has survived not only five centuries, but also the leap into electronic typesetting, remaining essentially unchanged. It was popularised in the 1960s with the release of Lettrline sheets containing Lorem Ipsum passages, and more recently with desktop publishing software like Pagewright including versions of Lorem Ipsum.</p>

<h2 class="abs center" style="top:530px">OUR SERVICES</h2>
<div class="abs service" style="left:77px">
  <h3>INDENTIFY</h3>
  <div class="photo" role="img" aria-label="Pen resting on banknotes and financial charts" style="background:linear-gradient(135deg,#cfd3cc,#f0f0ea 55%,#b9c2c4)"></div>
  <p>Lorem Ipsum is simply dummy text of the printing and typesetting industry. Lorem Ipsum has been the industry's standard dummy text ever since the 1500s, when an unknown printer took a galley of type and scrambled it to make a type specimen book.</p>
  <span class="more">READ MORE</span>
</div>
<div class="abs service" style="left:266px">
  <h3>PLAN</h3>
  <div class="photo" role="img" aria-label="Laptop keyboard with reading glasses" style="background:linear-gradient(135deg,#3a3a3a,#9a9a9a 45%,#f4f4f4 70%)"></div>
  <p>Lorem Ipsum is simply dummy text of the printing and typesetting industry. Lorem Ipsum has been the industry's standard dummy text ever since the 1500s, when an unknown printer took a galley of type and scrambled it to make a type specimen book.</p>
  <span class="more">READ MORE</span>
</div>
<div class="abs service" style="left:456px">
  <h3>RETIRE</h3>
  <div class="photo" role="img" aria-label="Hammock on a seaside porch under blue sky" style="background:linear-gradient(180deg,#8fb3d6,#c9d9e6 45%,#d8cfb8 65%,#8a7f6c)"></div>
  <p>Lorem Ipsum is simply dummy text of the printing and typesetting industry. Lorem Ipsum has been the industry's standard dummy text ever since the 1500s, when an unknown printer took a galley of type and scrambled it to make a type specimen book.</p>
  <span class="more">READ MORE</span>
</div>

<h2 class="abs" style="left:77px;top:821px">FEATURES</h2>
<div class="abs video" role="img" aria-label="Video of a smiling retired couple outdoors"></div>
<svg class="abs" style="left:78px;top:846px" width="330" height="178" viewBox="0 0 330 178">
  <rect x="146" y="79" width="38" height="25" rx="5" fill="#222" opacity=".85"/>
  <path d="M160 85l11 7-11 7z" fill="#fff"/>
  <rect x="16" y="153" width="298" height="18" rx="3" fill="#2b2b2b" opacity=".9"/>
  <rect x="24" y="159" width="196" height="6" rx="2" fill="#666"/>
  <rect x="24" y="159" width="60" height="6" rx="2" fill="#2fa8de"/>
  <rect x="228" y="158" width="28" height="8" fill="#2fa8de" opacity=".8"/>
  <text x="262" y="166" font-family="Open Sans,sans-serif" font-size="9" font-weight="700" font-style="italic" fill="#2fa8de">HD</text>
  <path d="M290 158l6 8M296 158l-6 8" stroke="#ddd" stroke-width="1.5"/>
</svg>
<ul class="abs features">
  <li><svg width="11" height="11" viewBox="0 0 11 11"><circle cx="5.5" cy="5.5" r="5.5" fill="#8fb03a"/><path d="M4 3l3 2.5L4 8" stroke="#fff" stroke-width="1.3" fill="none"/></svg><span>Identify and project your retirement needs and expectations including basic living expenses, housing costs, recreation, big ticket non-recurring items, medical and nursing home care.</span></li>
  <li><svg width="11" height="11" viewBox="0 0 11 11"><circle cx="5.5" cy="5.5" r="5.5" fill="#8fb03a"/><path d="M4 3l3 2.5L4 8" stroke="#fff" stroke-width="1.3" fill="none"/></svg><span>Identify and project all your sources of retirement income including retirement savings, other savings, pension plans, Social Security, life insurance and working part-time during retirement for a period of time.</span></li>
  <li><svg width="11" height="11" viewBox="0 0 11 11"><circle cx="5.5" cy="5.5" r="5.5" fill="#8fb03a"/><path d="M4 3l3 2.5L4 8" stroke="#fff" stroke-width="1.3" fill="none"/></svg><span>Strategize tapping into the equity of your real estate including swapping your primary residence for a different home or retirement area, or selling and renting.</span></li>
  <li><svg width="11" height="11" viewBox="0 0 11 11"><circle cx="5.5" cy="5.5" r="5.5" fill="#8fb03a"/><path d="M4 3l3 2.5L4 8" stroke="#fff" stroke-width="1.3" fill="none"/></svg><span>Produce easy to understand results featuring the Readiness Gauge™.</span></li>
  <li><svg width="11" height="11" viewBox="0 0 11 11"><circle cx="5.5" cy="5.5" r="5.5" fill="#8fb03a"/><path d="M4 3l3 2.5L4 8" stroke="#fff" stroke-width="1.3" fill="none"/></svg><span>Save your work so you can return, revisit and edit your retirement plan at a later date.</span></li>
</ul>

<h2 class="abs center" style="top:1055px">TESTIMONIALS</h2>
<p class="abs center quote">“This site is a great place to get a handle on your retirement strategy”, <span class="who">Dana, <b>Vermont</b></span></p>

<footer class="abs footer"></footer>
<div class="abs foot-links">HOME &nbsp;| &nbsp;ABOUT US &nbsp;| &nbsp;SERVICES &nbsp;| &nbsp;FAQ'S &nbsp;| &nbsp;CONTACT</div>
<div class="abs copyright">COPYRIGHT ©2013 COMPANY NAME &nbsp;- ALL RIGHTS RESERVED</div>
<span class="abs social" style="left:595px"></span>
<span class="abs social" style="left:621px"></span>
</body>
</html>
```